Tarvimoor business cards

Need fresh design for our business cards. Logo must be specific, we are open for everything else.

Contact Information for Business Card

phrase "GMP & JANITORIAL SERVICES" should be used as main point of card

Colors
3176b5
3276b5
85acd3
cedeed
ffffff
0292cd
33a6d7
85cae6
cee9f5

Requirements
Must have
• The logo
Should not have
• crowded designs

```html
<!DOCTYPE html>
<html lang="en">
<head>
<meta charset="utf-8">
<title>Tarvimoor Business Cards</title>
<link rel="stylesheet" href="https://fonts.googleapis.com/css2?family=PT+Sans:wght@400;700&family=PT+Sans+Narrow:wght@400&display=swap">
<style>
  :root {
    --backdrop: #373b3f;
    --brand-blue: #0381c2;
    --paper: #ffffff;
    --ink: #1b1b1b;
    --shadow: rgba(0, 0, 0, 0.55);
  }
  * { margin: 0; padding: 0; box-sizing: border-box; }
  html, body { width: 1200px; height: 2165px; overflow: hidden; }
  body { background: var(--backdrop); position: relative; font-family: "PT Sans", sans-serif; }

  .card {
    position: absolute;
    left: 105px;
    width: 985px;
    height: 563px;
    border-radius: 38px;
    overflow: hidden;
    box-shadow: 4px 12px 6px var(--shadow);
  }
  .card--front { top: 920px; background: var(--paper); }
  .card--back { top: 1527px; background: var(--brand-blue); }

  .card__wave { position: absolute; inset: 0; width: 100%; height: 100%; }

  .wordmark {
    position: absolute;
    font-family: "PT Sans", sans-serif;
    font-weight: 400;
    letter-spacing: 0.16em;
    white-space: nowrap;
  }
  .card--front .wordmark {
    left: 92px; top: 182px;
    font-size: 54px;
    color: var(--brand-blue);
  }
  .card--back .wordmark {
    left: 0; right: 0; top: 198px;
    text-align: center;
    font-size: 62px;
    color: var(--paper);
    padding-left: 0.16em;
  }

  .contact { position: absolute; left: 592px; top: 110px; }
  .contact__name {
    font-weight: 700;
    font-size: 43px;
    color: var(--brand-blue);
    line-height: 1;
    margin-bottom: 26px;
  }
  .contact__list { list-style: none; }
  .contact__item {
    display: flex; align-items: center;
    font-size: 31px; color: var(--ink);
    height: 49px;
  }
  .contact__icon { width: 32px; height: 32px; margin-right: 12px; flex: none; }

  .service-tag {
    position: absolute;
    left: 50%; top: 303px;
    transform: translateX(-50%);
    width: 454px; height: 49px;
    background: var(--paper);
    color: var(--brand-blue);
    font-family: "PT Sans Narrow", sans-serif;
    font-size: 35px;
    line-height: 49px;
    text-align: center;
    white-space: nowrap;
  }
</style>
</head>
<body>

  <section class="card card--front" aria-label="Business card front">
    <svg class="card__wave" viewBox="0 0 985 563" preserveAspectRatio="none" aria-hidden="true">
      <path d="M0,390 C120,330 260,320 420,360 S700,470 800,455 S950,400 985,358" fill="none" stroke="var(--brand-blue)" stroke-width="17"/>
      <path d="M0,433 C120,372 260,366 420,405 S700,496 800,488 S950,442 985,400 L985,563 L0,563 Z" fill="var(--brand-blue)"/>
    </svg>

    <div class="wordmark">TARVIMOOR</div>

    <div class="contact">
      <p class="contact__name">Your Namehere</p>
      <ul class="contact__list">
        <li class="contact__item">
          <svg class="contact__icon" viewBox="0 0 32 32" aria-hidden="true">
            <circle cx="16" cy="16" r="16" fill="var(--brand-blue)"/>
            <path d="M11 8.5c1-.6 2-.2 2.5.8l1.2 2.5c.4.8.1 1.6-.5 2.1l-1 .8c.8 2 2.2 3.4 4.1 4.3l.9-1c.6-.6 1.4-.8 2.1-.4l2.5 1.3c.9.5 1.2 1.6.6 2.5-1 1.6-2.8 2.4-4.6 1.8-4.6-1.5-8-5-9.4-9.6-.5-1.8.3-3.6 1.6-4.4z" fill="var(--paper)"/>
          </svg>
          1 (866) 555-0148
        </li>
        <li class="contact__item">
          <svg class="contact__icon" viewBox="0 0 32 32" aria-hidden="true">
            <circle cx="16" cy="16" r="16" fill="var(--brand-blue)"/>
            <rect x="11" y="8" width="10" height="6" fill="var(--paper)"/>
            <rect x="7.5" y="13" width="17" height="8" rx="2" fill="var(--paper)"/>
            <rect x="11" y="18" width="10" height="6" fill="var(--paper)" stroke="var(--brand-blue)" stroke-width="1.5"/>
          </svg>
          (905) 555-0172
        </li>
        <li class="contact__item">
          <svg class="contact__icon" viewBox="0 0 32 32" aria-hidden="true">
            <circle cx="16" cy="16" r="16" fill="var(--brand-blue)"/>
            <rect x="8" y="10" width="16" height="12" rx="1.5" fill="var(--paper)"/>
            <path d="M8.8 11l7.2 6 7.2-6" fill="none" stroke="var(--brand-blue)" stroke-width="1.8"/>
          </svg>
          info@tarvimoor.ca
        </li>
      </ul>
    </div>
  </section>

  <section class="card card--back" aria-label="Business card back">
    <div class="wordmark">TARVIMOOR</div>
    <p class="service-tag">GMP &amp; JANITORIAL SERVICES</p>
  </section>

</body>
</html>
```